Lantern Path Collective

Re-design our website www.lanternpathco.org
We are a non profit catering for adults, elderly, veterans and youth in impoverished neighborhoods to improve their digital access and help them improve their lives and better our community.

I need the text on home page to stay. Its the first message vsitors shd read when they arrive on our page.

Number of Pages Required

4 page

Font styles to use
Other font styles liked:
• color and font shd be like the image attched below.

```html
<!DOCTYPE html>
<html lang="en">
<head>
<meta charset="utf-8">
<title>Lantern Path Collective</title>
<link rel="stylesheet" href="https://fonts.googleapis.com/css2?family=Poppins:wght@300;400;500;600;700&display=swap">
<style>
:root{
  --blue:#3d8be6;
  --blue-deep:#2f6fdc;
  --blue-light:#8cc0ee;
  --navy:#0d2c6b;
  --ink:#2e3a5a;
  --text:#444b5c;
  --orange:#f6a562;
  --orange-deep:#f39244;
  --green:#a9d35a;
  --white:#ffffff;
  --pale:#e8edf6;
}
*{margin:0;padding:0;box-sizing:border-box}
html,body{width:1200px;height:3812px;overflow:hidden}
body{position:relative;font-family:"Poppins",sans-serif;color:var(--text);background:var(--white)}
.abs{position:absolute}
a{color:inherit;text-decoration:none}

/* header */
.topbar{left:570px;top:0;width:630px;height:37px;display:flex;font-size:13px;color:#fff}
.topbar .mail{background:var(--blue);width:290px;display:flex;align-items:center;padding-left:30px;gap:8px;clip-path:polygon(6% 0,100% 0,100% 100%,0 100%)}
.topbar .call{background:var(--orange);flex:1;display:flex;align-items:center;padding-left:30px;gap:8px;font-weight:600}
.ico{width:24px;height:24px;border-radius:50%;background:#fff;display:inline-flex;align-items:center;justify-content:center}
.brand{left:104px;top:12px;width:140px;height:130px;border-radius:50%;background:#fff;display:flex;align-items:center;justify-content:center;text-align:center;font-size:15px;font-weight:600;color:var(--blue);line-height:1.25;z-index:3}
.nav{left:310px;top:62px;display:flex;gap:34px;font-size:14px;color:var(--ink);align-items:center}
.nav .active{color:var(--blue);border-bottom:2px solid var(--blue);padding-bottom:8px;margin-top:10px}
.btn-donate{left:983px;top:57px;width:112px;height:34px;border-radius:17px;background:var(--green);color:#fff;font-size:14px;display:flex;align-items:center;justify-content:center}

/* hero */
.hero{left:0;top:111px;width:1200px;height:600px;background:linear-gradient(100deg,var(--blue-deep) 0%,#4a95ea 55%,#9ac8f0 100%)}
.hero h1{left:70px;top:185px;width:480px;text-align:center;color:#fff;font-size:39px;font-weight:700;line-height:1.0}
.hero .sub{left:90px;top:282px;width:440px;text-align:center;color:#fff;font-size:18px;line-height:1.55}
.btn{display:flex;align-items:center;justify-content:center;color:#fff;font-weight:500;font-size:15px;border-radius:26px;letter-spacing:.3px}
.hero .cta{left:219px;top:359px;width:178px;height:51px;background:var(--orange)}
.hero-photo{left:660px;top:95px;width:430px;height:520px;border-radius:200px 200px 40px 40px;background:linear-gradient(180deg,#f2c8a8 0%,#e9a7b7 45%,#8f9db5 80%,#cfd7e6 100%);opacity:.9}
.feature{color:#fff;font-size:15px;font-weight:600;line-height:1.2;text-align:center}
.dot{width:62px;height:62px;border-radius:50%;border:3px solid rgba(255,255,255,.6);display:flex;align-items:center;justify-content:center}

/* about */
.bubble{position:absolute;border-radius:50%;color:#fff;text-align:center;display:flex;flex-direction:column;align-items:center;justify-content:flex-start}
.bubble h3{font-size:20px;font-weight:600;line-height:1.2;margin:6px 0 4px}
.bubble .blurb{font-size:10.5px;line-height:16px;width:160px;color:#fff}
.mission{padding-top:42px}
.vision{padding-top:42px}
.donate{padding-top:42px}
.eyebrow{font-size:14px;color:var(--blue);letter-spacing:.3px}
.about h2{font-size:38px;font-weight:400;color:var(--ink);letter-spacing:.5px}
.about h2 b{font-weight:700}
.rule{width:46px;height:3px;background:var(--orange)}
.about .intro{font-size:16px;line-height:28.6px;color:var(--text)}
.kids{left:0;top:1228px;width:1200px;height:373px;background:linear-gradient(90deg,#d9d3cb 0%,#c8b7a4 30%,#b9c8d5 55%,#9ebf8f 75%,#d8c4b9 100%)}

/* services */
.services{left:0;top:1601px;width:1200px;height:540px;background:linear-gradient(180deg,var(--blue-deep) 0%,#4f97e9 60%,#8cbfee 100%)}
.services .label{top:70px;width:100%;text-align:center;color:#fff;font-size:13px}
.services h2{top:100px;width:100%;text-align:center;color:#fff;font-size:31px;font-weight:600;line-height:38px}
.services p{top:238px;left:190px;width:820px;text-align:center;color:#fff;font-size:15px;line-height:24px}
.card{width:237px;height:262px;background:#fff;border-radius:60px 60px 0 60px;box-shadow:0 8px 22px rgba(40,80,150,.15);padding:72px 20px 0 35px}
.card h4{font-size:15px;font-weight:600;color:var(--ink);line-height:21px}
.card p{font-size:10px;line-height:14.5px;color:#777;margin-top:8px}
.card .more{margin-top:12px;width:104px;height:26px;border-radius:13px;color:#fff;font-size:9px;font-weight:600;display:flex;align-items:center;justify-content:center}
.card-icon{width:82px;height:82px;border-radius:50%;border:4px solid #fff;box-shadow:0 4px 12px rgba(0,0,0,.12);display:flex;align-items:center;justify-content:center}

/* impact */
.impact h2{font-size:36px;font-weight:700;color:var(--ink)}
.impact h3{font-size:26px;font-weight:400;color:var(--blue)}
.impact p{font-size:15.5px;line-height:26px;color:var(--text)}
.impact-photo{left:621px;top:2380px;width:460px;height:373px;border-radius:14px;background:linear-gradient(135deg,#8a6a55 0%,#c59a7c 40%,#e9c9ae 70%,#f1ede8 100%)}
.impact-frame{left:612px;top:2372px;width:467px;height:382px;border:2px solid var(--orange);border-radius:16px}

/* contact */
.contact{left:0;top:2868px;width:1200px;height:600px;background:linear-gradient(110deg,var(--blue-deep) 0%,#4d93e8 60%,#8fc0ee 100%)}
.field{background:#fff;color:#666;font-size:14px;padding:0 18px;display:flex;align-items:center}
.send{left:510px;top:3252px;width:184px;height:45px;background:var(--navy);font-weight:600}

/* footer */
.fcol h5{font-size:14px;font-weight:600;color:var(--ink);margin-bottom:12px;border-left:3px solid var(--blue);padding-left:20px;margin-left:-22px}
.fcol li{list-style:none;font-size:10.5px;color:#444;line-height:22px}
.vline{width:1px;height:170px;background:#d9dee8}
.copy{left:0;top:3714px;width:1200px;height:98px;background:var(--pale);display:flex;align-items:center;justify-content:center;font-size:10px;color:#444;padding-top:30px}
.crow{display:flex;align-items:center;gap:10px;font-size:11px;color:#333;margin-bottom:8px}
.crow .c{width:22px;height:22px;border-radius:50%;background:var(--blue);display:flex;align-items:center;justify-content:center}
</style>
</head>
<body>

<!-- header -->
<div class="abs topbar">
  <div class="mail"><span class="ico"><svg width="12" height="9" viewBox="0 0 12 9"><rect x=".5" y=".5" width="11" height="8" fill="none" stroke="#3d8be6"/><path d="M.5 .5 6 5l5.5-4.5" fill="none" stroke="#3d8be6"/></svg></span>info@lanternpathco.org</div>
  <div class="call"><span class="ico"><svg width="12" height="12" viewBox="0 0 24 24"><path fill="#f6a562" d="M6.6 10.8c1.4 2.8 3.8 5.1 6.6 6.6l2.2-2.2c.3-.3.7-.4 1-.2 1.1.4 2.3.6 3.6.6.6 0 1 .4 1 1V20c0 .6-.4 1-1 1C10.6 21 3 13.4 3 4c0-.6.4-1 1-1h3.5c.6 0 1 .4 1 1 0 1.3.2 2.5.6 3.6.1.3 0 .7-.2 1z"/></svg></span>Call Us: (555) 010-0142</div>
</div>
<div class="abs brand">Lantern Path<br>Collective</div>
<nav class="abs nav">
  <a class="active">Home</a><a>Get Connected</a><a>e-Waste Services</a><a>Our Impact</a><a>About</a><a>Contact</a>
</nav>
<a class="abs btn-donate">Donate</a>

<!-- hero -->
<section class="abs hero">
  <svg class="abs" style="left:0;bottom:0" width="1200" height="220" viewBox="0 0 1200 220" preserveAspectRatio="none">
    <path d="M0 90 C150 20 320 160 520 120 S860 40 1200 120 V220 H0Z" fill="#ffffff" opacity=".18"/>
    <path d="M0 150 C180 80 360 200 560 170 S900 110 1200 170 V220 H0Z" fill="#ffffff" opacity=".35"/>
    <path d="M0 200 C220 150 420 220 640 200 S960 170 1200 205 V220 H0Z" fill="#ffffff"/>
  </svg>
  <svg class="abs" style="left:560px;top:90px" width="560" height="420" viewBox="0 0 560 420"><path d="M40 380 A260 260 0 0 1 480 120" fill="none" stroke="rgba(255,255,255,.45)" stroke-width="2"/></svg>
  <div class="abs hero-photo" role="img" aria-label="Smiling girl sitting cross-legged with a laptop"></div>
  <h1 class="abs">CREATING A SOCIAL IMPACT WITH E-WASTE</h1>
  <p class="abs sub">by transforming Unwanted Technology into Opportunities for People In-Need.</p>
  <a class="abs btn cta">LEARN MORE</a>

  <div class="abs feature" style="left:600px;top:95px;width:130px">INTERNET<br>ACCESS</div>
  <div class="abs dot" style="left:634px;top:136px;background:var(--orange)"><svg width="30" height="24" viewBox="0 0 30 24" fill="none" stroke="#fff" stroke-width="2.4" stroke-linecap="round"><path d="M3 9a17 17 0 0 1 24 0M7.5 13.5a10.5 10.5 0 0 1 15 0M11.5 17.5a4.5 4.5 0 0 1 7 0"/><circle cx="15" cy="21" r="1.3" fill="#fff"/></svg></div>
  <div class="abs feature" style="left:855px;top:92px;width:160px">DIGITAL LITERACY<br>TRAINING</div>
  <div class="abs dot" style="left:898px;top:133px;background:var(--green)"><svg width="24" height="28" viewBox="0 0 24 28" fill="none" stroke="#fff" stroke-width="2.2"><path d="M12 2a8 8 0 0 0-5 14v4h10v-4a8 8 0 0 0-5-14z"/><path d="M8 24h8"/></svg></div>
  <div class="abs dot" style="left:947px;top:259px;background:var(--blue)"><svg width="28" height="28" viewBox="0 0 28 28" fill="none" stroke="#fff" stroke-width="2.2"><circle cx="14" cy="12" r="6"/><path d="M4 26c2-6 18-6 20 0M5 12a9 9 0 0 1 18 0"/></svg></div>
  <div class="abs feature" style="left:1016px;top:269px;text-align:left">TECH<br>SUPPORT</div>
  <div class="abs feature" style="left:556px;top:281px;width:120px;font-size:14px">AFFORDABLE<br>TECHNOLOGY</div>
  <div class="abs dot" style="left:593px;top:333px;background:rgba(255,255,255,.25)"><svg width="30" height="24" viewBox="0 0 30 24" fill="none" stroke="#fff" stroke-width="2"><rect x="4" y="3" width="22" height="14" rx="1"/><path d="M1 21h28"/></svg></div>
</section>

<!-- about -->
<section class="about">
  <div class="bubble mission" style="left:89px;top:800px;width:244px;height:244px;background:linear-gradient(135deg,#f7b36f,#f3903f)">
    <svg width="48" height="48" viewBox="0 0 48 48" fill="none" stroke="#fff" stroke-width="2.4"><circle cx="24" cy="24" r="20"/><circle cx="24" cy="24" r="12"/><circle cx="24" cy="24" r="4"/><path d="M24 24 40 8M34 8h6v6"/></svg>
    <h3>Our Mission</h3><p class="blurb">Lantern Path Collective's mission is to tackle two</p>
  </div>
  <div class="bubble vision" style="left:310px;top:844px;width:248px;height:248px;background:linear-gradient(135deg,#b7dc6a,#9ccb4b)">
    <svg width="50" height="40" viewBox="0 0 50 40" fill="none" stroke="#fff" stroke-width="2.4"><path d="M3 20s8-12 22-12 22 12 22 12-8 12-22 12S3 20 3 20z"/><circle cx="25" cy="20" r="6"/></svg>
    <h3>Our Vision</h3><p class="blurb" style="width:180px">Lantern Path Collective's mission is to tackle two problems</p>
  </div>
  <div class="bubble donate" style="left:170px;top:990px;width:248px;height:248px;background:linear-gradient(135deg,#5ea3ec,#2f75e0)">
    <svg width="40" height="54" viewBox="0 0 40 54" fill="none" stroke="#fff" stroke-width="2.4"><circle cx="20" cy="12" r="9"/><path d="M20 8v8"/><rect x="3" y="24" width="34" height="26" rx="2"/><path d="M20 44s-9-5-9-10a4.5 4.5 0 0 1 9-1 4.5 4.5 0 0 1 9 1c0 5-9 10-9 10z"/></svg>
    <h3>Donate Now</h3><p class="blurb" style="width:190px">Lantern Path Collective's mission is to tackle two problems</p>
  </div>
  <div class="abs eyebrow" style="left:620px;top:835px">WHO WE ARE</div>
  <h2 class="abs" style="left:620px;top:855px">ABOUT <b>LANTERN PATH</b></h2>
  <div class="abs rule" style="left:620px;top:907px"></div>
  <p class="abs intro" style="left:620px;top:927px;width:480px">A charitable organization, Open Harbor Initiative DBA Lantern Path Collective, is based in Los Angeles, California. The focus of Lantern Path Collective is to provide programs and services that empower and uplift people, providing the opportunity to advance their knowledge and develop lifelong skills while creating positive change.</p>
  <a class="abs btn" style="left:614px;top:1130px;width:179px;height:48px;background:var(--blue)">LEARN MORE</a>
</section>
<div class="abs kids" role="img" aria-label="Row of five children using laptops at a classroom table"></div>

<!-- services -->
<section class="abs services">
  <div class="abs label">ONLINE TECHNOLOGY</div>
  <h2 class="abs">EXPLORE OPPORTUNITIES ONLINE WITH<br>LOW-COST TECHNOLOGY, INTERNET,<br>TRAINING &amp; SUPPORT</h2>
  <div class="abs rule" style="left:577px;top:220px"></div>
  <p class="abs">In order to comprehensively shrink the digital divide, we offer you access to low-cost computers, low-cost internet, free digital literacy training and tech support. Click the boxes below to explore how we can help you and members of your community unlock their full potential through digital technology.</p>
  <svg class="abs" style="left:0;bottom:0" width="1200" height="140" viewBox="0 0 1200 140" preserveAspectRatio="none"><path d="M0 20 C250 100 500 0 760 50 S1050 110 1200 40 V140 H0Z" fill="#fff"/></svg>
</section>
<svg class="abs" style="left:1000px;top:2160px" width="140" height="120" viewBox="0 0 140 120"><g fill="#b9c7e0"><circle cx="100" cy="5" r="1.6"/><circle cx="115" cy="5" r="1.6"/><circle cx="130" cy="5" r="1.6"/><circle cx="100" cy="25" r="1.6"/><circle cx="115" cy="25" r="1.6"/><circle cx="130" cy="25" r="1.6"/><circle cx="100" cy="45" r="1.6"/><circle cx="115" cy="45" r="1.6"/><circle cx="130" cy="45" r="1.6"/><circle cx="10" cy="100" r="1.6"/><circle cx="25" cy="100" r="1.6"/><circle cx="40" cy="100" r="1.6"/><circle cx="55" cy="100" r="1.6"/><circle cx="70" cy="100" r="1.6"/><circle cx="85" cy="100" r="1.6"/><circle cx="100" cy="100" r="1.6"/><circle cx="115" cy="100" r="1.6"/><circle cx="130" cy="100" r="1.6"/><circle cx="10" cy="115" r="1.6"/><circle cx="40" cy="115" r="1.6"/><circle cx="70" cy="115" r="1.6"/><circle cx="100" cy="115" r="1.6"/><circle cx="130" cy="115" r="1.6"/></g></svg>

<div class="abs card" style="left:111px;top:1990px"><h4>AFFORDABLE<br>TECHNOLOGY</h4><p>Lorem Ipsum is simply dummy text of the printing and typeset-ting industry. Lorem Ipsum has been the industry's standard</p><a class="more" style="background:var(--blue)">LEARN MORE</a></div>
<div class="abs card" style="left:362px;top:1990px"><h4>INTERNET<br>ACCESS</h4><p>Lorem Ipsum is simply dummy text of the printing and typeset-ting industry. Lorem Ipsum has been the industry's standard</p><a class="more" style="background:#c1dd8f">LEARN MORE</a></div>
<div class="abs card" style="left:614px;top:1990px"><h4>DIGITAL LITERACY<br>TRAINING</h4><p>Lorem Ipsum is simply dummy text of the printing and typeset-ting industry. Lorem Ipsum has been the industry's standard</p><a class="more" style="background:var(--orange)">LEARN MORE</a></div>
<div class="abs card" style="left:866px;top:1990px"><h4>TECH<br>SUPPORT</h4><p>Lorem Ipsum is simply dummy text of the printing and typeset-ting industry. Lorem Ipsum has been the industry's standard</p><a class="more" style="background:var(--blue-light)">LEARN MORE</a></div>

<div class="abs card-icon" style="left:136px;top:1953px;background:var(--blue)"><svg width="40" height="32" viewBox="0 0 40 32" fill="none" stroke="#fff" stroke-width="2.2"><rect x="5" y="3" width="30" height="20" rx="1"/><path d="M1 29h38M22 14l6 5"/></svg></div>
<div class="abs card-icon" style="left:391px;top:1953px;background:var(--green)"><svg width="36" height="28" viewBox="0 0 30 24" fill="none" stroke="#fff" stroke-width="2.4" stroke-linecap="round"><path d="M3 9a17 17 0 0 1 24 0M7.5 13.5a10.5 10.5 0 0 1 15 0M11.5 17.5a4.5 4.5 0 0 1 7 0"/><circle cx="15" cy="21" r="1.3" fill="#fff"/></svg></div>
<div class="abs card-icon" style="left:641px;top:1953px;background:var(--orange)"><svg width="30" height="36" viewBox="0 0 24 28" fill="none" stroke="#fff" stroke-width="2.2"><path d="M12 2a8 8 0 0 0-5 14v4h10v-4a8 8 0 0 0-5-14z"/><path d="M8 24h8"/></svg></div>
<div class="abs card-icon" style="left:893px;top:1953px;background:var(--blue-light)"><svg width="34" height="34" viewBox="0 0 28 28" fill="none" stroke="#fff" stroke-width="2.2"><circle cx="14" cy="12" r="6"/><path d="M4 26c2-6 18-6 20 0M5 12a9 9 0 0 1 18 0"/></svg></div>

<!-- impact -->
<section class="impact">
  <h2 class="abs" style="left:133px;top:2400px">OUR IMPACT</h2>
  <h3 class="abs" style="left:133px;top:2462px">Lantern Path Collective</h3>
  <p class="abs" style="left:133px;top:2508px;width:400px">We start by diverting e-waste from landfills and end with more connected communities.</p>
  <p class="abs" style="left:133px;top:2575px;width:400px">Every day the opportunity gap between those with access to technology and those without it widens. Our world continues to move more and more online–educational opportunities</p>
  <a class="abs btn" style="left:133px;top:2693px;width:175px;height:46px;background:var(--blue-light)">LEARN MORE</a>
  <svg class="abs" style="left:575px;top:2630px" width="170" height="160" viewBox="0 0 170 160"><g fill="#b9c7e0"><circle cx="4" cy="4" r="1.6"/><circle cx="19" cy="4" r="1.6"/><circle cx="4" cy="24" r="1.6"/><circle cx="19" cy="24" r="1.6"/><circle cx="4" cy="44" r="1.6"/><circle cx="19" cy="44" r="1.6"/><circle cx="4" cy="64" r="1.6"/><circle cx="19" cy="64" r="1.6"/><circle cx="4" cy="84" r="1.6"/><circle cx="19" cy="84" r="1.6"/><circle cx="4" cy="104" r="1.6"/><circle cx="19" cy="104" r="1.6"/><circle cx="4" cy="124" r="1.6"/><circle cx="34" cy="124" r="1.6"/><circle cx="64" cy="124" r="1.6"/><circle cx="94" cy="124" r="1.6"/><circle cx="124" cy="124" r="1.6"/><circle cx="154" cy="124" r="1.6"/><circle cx="4" cy="144" r="1.6"/><circle cx="34" cy="144" r="1.6"/><circle cx="64" cy="144" r="1.6"/><circle cx="94" cy="144" r="1.6"/><circle cx="124" cy="144" r="1.6"/><circle cx="154" cy="144" r="1.6"/></g></svg>
  <div class="abs impact-frame"></div>
  <div class="abs impact-photo" role="img" aria-label="Three children smiling together at a laptop"></div>
</section>

<!-- contact -->
<section class="abs contact">
  <div class="abs" style="top:83px;width:100%;text-align:center;color:#fff;font-size:11px">GET IN TOUCH WITH US</div>
  <h2 class="abs" style="top:100px;width:100%;text-align:center;color:#fff;font-size:30px;font-weight:600">CONTACT US</h2>
  <div class="abs rule" style="left:577px;top:148px"></div>
  <svg class="abs" style="left:0;bottom:0" width="1200" height="110" viewBox="0 0 1200 110" preserveAspectRatio="none"><path d="M0 60 C200 20 420 90 620 55 S960 20 1200 60 V110 H0Z" fill="#fff" opacity=".35"/><path d="M0 85 C240 50 460 105 660 78 S1000 55 1200 85 V110 H0Z" fill="#fff"/></svg>
</section>
<div class="abs field" style="left:281px;top:3027px;width:317px;height:46px">First Name*</div>
<div class="abs field" style="left:607px;top:3027px;width:318px;height:46px">Last Name*</div>
<div class="abs field" style="left:281px;top:3083px;width:317px;height:46px">Phone Number*</div>
<div class="abs field" style="left:607px;top:3083px;width:318px;height:46px">Email address*</div>
<div class="abs field" style="left:281px;top:3140px;width:644px;height:93px;align-items:flex-start;padding-top:12px">Message</div>
<a class="abs btn send">SEND ENQUIRY</a>

<!-- footer -->
<footer>
  <div class="abs" style="left:118px;top:3560px;width:140px;text-align:center;font-size:18px;font-weight:600;color:var(--blue);line-height:1.3">Lantern Path<br>Collective</div>
  <div class="abs vline" style="left:318px;top:3510px"></div>
  <div class="abs vline" style="left:507px;top:3510px"></div>
  <div class="abs vline" style="left:678px;top:3510px"></div>
  <div class="abs vline" style="left:843px;top:3510px"></div>
  <div class="abs fcol" style="left:341px;top:3543px"><h5>NAVIGATION</h5><ul><li>Get Technology</li><li>Low-Cost Internet</li><li>Digital Training</li><li>Tech Support</li><li>For Organizations</li></ul></div>
  <div class="abs fcol" style="left:529px;top:3547px"><h5>RESOURCES</h5><ul><li>E-Waste Services</li><li>Data Destruction</li><li>Technology Drives</li></ul></div>
  <div class="abs fcol" style="left:697px;top:3547px"><h5>COMPANY</h5><ul><li>About Us</li><li>Our Impact</li><li>Mission</li><li>Vision</li></ul></div>
  <div class="abs fcol" style="left:867px;top:3545px"><h5>CONTACT US</h5>
    <div class="crow"><span class="c"><svg width="11" height="11" viewBox="0 0 24 24"><path fill="#fff" d="M6.6 10.8c1.4 2.8 3.8 5.1 6.6 6.6l2.2-2.2c.3-.3.7-.4 1-.2 1.1.4 2.3.6 3.6.6.6 0 1 .4 1 1V20c0 .6-.4 1-1 1C10.6 21 3 13.4 3 4c0-.6.4-1 1-1h3.5c.6 0 1 .4 1 1 0 1.3.2 2.5.6 3.6.1.3 0 .7-.2 1z"/></svg></span>(555) 010-0142</div>
    <div class="crow"><span class="c"><svg width="11" height="9" viewBox="0 0 12 9"><rect x=".5" y=".5" width="11" height="8" fill="none" stroke="#fff"/><path d="M.5 .5 6 5l5.5-4.5" fill="none" stroke="#fff"/></svg></span>info@lanternpathco.org</div>
    <div class="crow"><span class="c"><svg width="10" height="13" viewBox="0 0 10 13"><path fill="#fff" d="M5 0a5 5 0 0 0-5 5c0 3.5 5 8 5 8s5-4.5 5-8a5 5 0 0 0-5-5zm0 7a2 2 0 1 1 0-4 2 2 0 0 1 0 4z"/></svg></span>118 Lantern Row, Fairview, CA 90210</div>
  </div>
  <div class="abs copy">Copyright © 2022 <u style="margin:0 3px">Lantern Path</u> All Rights Reserved</div>
</footer>

</body>
</html>
```